Welding Fabrication and Inspection Business Card Design

Welding Fabrication and Inspection Services,

Business

Industrial Machinery ServicesMohammed Rahim30 Ballarat Street, Mount Gravatt East.4122.QLD

```html
<!DOCTYPE html>
<html lang="en">
<head>
<meta charset="utf-8">
<title>Tarnwell Forge Services – Business Card</title>
<link rel="stylesheet" href="https://fonts.googleapis.com/css2?family=Lato:wght@400;700;900&display=swap">
<style>
  :root {
    --bg: #e9e7e4;
    --card: #ffffff;
    --ink: #1c1c1c;
    --band-dark: #2e2d30;
    --band-light: #8a898c;
    --accent: #8e1c1f;
    --rule: #b9b9b9;
    --tool-a: #8c2b33;
    --tool-b: #3a1a1d;
  }
  * { box-sizing: border-box; margin: 0; padding: 0; }
  html, body { width: 1200px; height: 913px; overflow: hidden; }
  body {
    background: var(--bg);
    font-family: "Lato", sans-serif;
    color: var(--ink);
    position: relative;
  }
  .card {
    position: absolute;
    top: 300px;
    width: 540px;
    height: 310px;
    background: var(--card);
    box-shadow: 0 6px 18px rgba(0,0,0,0.18);
    overflow: hidden;
  }
  .card--front { left: 45px; }
  .card--back { left: 615px; }
  .card__band {
    position: absolute;
    left: 0; right: 0; bottom: 0;
    height: 24px;
    background: var(--band-dark);
    border-top: 5px solid var(--band-light);
  }
  .brand {
    position: absolute;
    display: flex;
    align-items: center;
    gap: 10px;
    font-weight: 900;
    font-size: 22px;
    color: var(--ink);
    white-space: nowrap;
  }
  .brand__dot {
    width: 14px; height: 14px;
    border-radius: 50%;
    background: var(--ink);
  }
  .card--front .brand { left: 50%; top: 128px; transform: translateX(-50%); }
  .card--back .brand { left: 28px; top: 126px; font-size: 18px; }
  .tool-photo {
    position: absolute;
    right: 34px; top: 30px;
    width: 92px; height: 52px;
    border-radius: 6px;
    background: linear-gradient(135deg, var(--tool-a), var(--tool-b));
  }
  .contact {
    position: absolute;
    left: 250px; top: 150px;
    width: 270px;
    text-align: center;
  }
  .contact__name {
    font-size: 19px;
    font-weight: 400;
    letter-spacing: 0.5px;
    color: var(--accent);
    text-transform: uppercase;
  }
  .contact__rule {
    width: 130px;
    height: 1px;
    margin: 7px auto 12px;
    background: var(--rule);
  }
  .contact__address {
    font-size: 12px;
    color: var(--ink);
  }
</style>
</head>
<body>
  <section class="card card--front">
    <div class="brand"><span class="brand__dot"></span>Tarnwell Forge Services</div>
    <div class="card__band"></div>
  </section>

  <section class="card card--back">
    <div class="tool-photo" role="img" aria-label="Photo of a red handheld welding inspection tool"></div>
    <div class="brand"><span class="brand__dot"></span>Tarnwell Forge Services</div>
    <div class="contact">
      <p class="contact__name">Khalid Nasser</p>
      <div class="contact__rule"></div>
      <p class="contact__address">17 Corrowen Street, Halvern Ridge. 4187.QLD</p>
    </div>
    <div class="card__band"></div>
  </section>
</body>
</html>
```